construction company business card

I need a business card design for a new company called TK CREST WORKS. I'd like to see different designs with the name tk CREST WORKS, and others for TK Crest Works. The company field is Home Improvement and everything related with construction. Colors I like are red, blue and black. The final design should communicate/show simplicity and security.

Industry/Entity Type

Construction

Contact Information for Business Card

TK CREST WORKS
Tobias Kellner
(917)555-0143
57-31 226th Avenue
Birch Hollow
11562, NY

Requirements
Must have
• HOME IMPROVEMENT

```html
<!DOCTYPE html>
<html lang="en">
<head>
<meta charset="utf-8">
<title>TK Crest Works – Business Card</title>
<link rel="stylesheet" href="https://fonts.googleapis.com/css2?family=Oswald:wght@400;500;600;700&display=swap">
<style>
  :root {
    --stage: #1c1c1c;
    --card-dark: #0b0b0b;
    --card-light: #ffffff;
    --ink: #1a1a1a;
    --ink-soft: #bdbdbd;
    --accent: #e0262f;
    --accent-soft: #e86a6a;
  }
  * { box-sizing: border-box; margin: 0; padding: 0; }
  html, body {
    width: 1200px; height: 871px; overflow: hidden;
    background: var(--stage);
    font-family: "Oswald", "Arial Narrow", sans-serif;
  }
  .stage { position: relative; width: 1200px; height: 871px; }

  .card {
    position: absolute;
    width: 620px; height: 354px;
    border-radius: 4px;
    box-shadow: 0 14px 40px rgba(0,0,0,.55);
  }

  /* Front: black */
  .card--front {
    left: 80px; top: 80px;
    background: var(--card-dark);
    display: flex; flex-direction: column; align-items: center; justify-content: center;
  }
  .front-brand {
    color: var(--ink-soft);
    font-weight: 600;
    font-size: 54px;
    letter-spacing: 5px;
    line-height: 1;
  }
  .front-tagline {
    margin-top: 16px;
    color: var(--accent-soft);
    font-weight: 500;
    font-size: 24px;
    letter-spacing: 7px;
  }

  /* Back: white */
  .card--back {
    left: 500px; top: 437px;
    background: var(--card-light);
    display: flex; align-items: center;
    padding: 0 30px 0 46px;
  }
  .back-brand {
    width: 230px;
    color: var(--ink);
    font-weight: 600;
    font-size: 30px;
    letter-spacing: 2px;
    line-height: 1.15;
  }
  .back-divider {
    width: 2px; height: 168px;
    background: var(--accent);
    margin: 0 22px 0 16px;
  }
  .contact { color: var(--ink); }
  .contact-name {
    font-weight: 600; font-size: 26px; letter-spacing: 1px;
    margin-bottom: 6px;
  }
  .contact-row {
    display: flex; align-items: flex-start;
    font-weight: 500; font-size: 17px; line-height: 1.4;
    margin-top: 2px;
  }
  .contact-icon { width: 14px; height: 14px; margin: 5px 10px 0 0; flex: none; fill: var(--accent); }
</style>
</head>
<body>
<main class="stage">
  <section class="card card--front" aria-label="Card front">
    <div class="front-brand">TK CREST WORKS</div>
    <div class="front-tagline">HOME IMPROVEMENT</div>
  </section>

  <section class="card card--back" aria-label="Card back">
    <div class="back-brand">TK CREST WORKS</div>
    <div class="back-divider"></div>
    <div class="contact">
      <div class="contact-name">Tobias Kellner</div>
      <div class="contact-row">
        <svg class="contact-icon" viewBox="0 0 16 16" aria-hidden="true"><path d="M1 6c0-2 3-3 7-3s7 1 7 3v1h-3V5.5C11 5 10 5 8 5S5 5 4 5.5V7H1z"/><rect x="3" y="8" width="10" height="6" rx="1"/></svg>
        <span>(555) 555-0143</span>
      </div>
      <div class="contact-row">
        <svg class="contact-icon" viewBox="0 0 16 16" aria-hidden="true"><path d="M1 3h14v1L8 9 1 4z"/><path d="M1 6l7 5 7-5v7H1z"/></svg>
        <span>tkellner@tkcrestworks.com</span>
      </div>
      <div class="contact-row">
        <svg class="contact-icon" viewBox="0 0 16 16" aria-hidden="true"><path d="M8 0a5.5 5.5 0 0 0-5.5 5.5C2.5 10 8 16 8 16s5.5-6 5.5-10.5A5.5 5.5 0 0 0 8 0zm0 8a2.5 2.5 0 1 1 0-5 2.5 2.5 0 0 1 0 5z"/></svg>
        <span>57-31 226th Avenue<br>Birch Hollow, 11562, NY</span>
      </div>
    </div>
  </section>
</main>
</body>
</html>
```